Rock, Paper Scissors Championship Flyer

We need a dynamic, bold and exciting flyer to promote the following event at our sports center. The event will be primarily focused for adults, but children are welcome to join

Rock, Paper, Scissors Championship - $$$ prizes
Date: June 9th, 2018
Time: 11am-4pm
Fee: $2 to enter, free for spectators
Heats to determine the overall ‘Rock, Paper, Scissors’ champion!
- Cash prizes on offer
- Live music.
- Food and beverage available for purchase

Belvorrow Sports Center, Roselle NJ
908-555-3162
www.belvorrowgrounds.example

Must include our logo (does not have to be huge) and County seal (both attached)

Colors

Designer to choose colors to be used in the design.

Requirements
Must have
• Should be fun and colorful
• The following info and attached logos:
• Rock, Paper, Scissors Championship - $$$ prizes
• Date: June 9th, 2018
• Time: 11am-4pm
• Fee: $2 to enter, free for spectators
• Heats to determine the overall ‘Rock, Paper, Scissors’ champion!
• - Cash prizes on offer
• - Live music.
• - Food and beverage available for purchase
• Belvorrow Sports Center, Roselle NJ
• 908-555-3162
• www.belvorrowgrounds.example
Nice to have
• There are a few inspirational photos attached to give an idea of what we are looking for.

```html
<!DOCTYPE html>
<html lang="en">
<head>
<meta charset="utf-8">
<title>Rock Paper Scissors Championship Flyer</title>
<link href="https://fonts.googleapis.com/css2?family=Oswald:wght@500;600&family=Roboto+Condensed:wght@400;700&family=Open+Sans:wght@600;700;800&display=swap" rel="stylesheet">
<style>
  :root {
    --teal: #13a394;
    --teal-dark: #0d8a7d;
    --teal-light: #5fd0c4;
    --lime: #b8d930;
    --lime-pale: #e4f08a;
    --yellow: #d9e84a;
    --orange: #f7a823;
    --cream: #f3f8e2;
    --ink: #4a4a4a;
    --white: #ffffff;
  }
  * { margin: 0; padding: 0; box-sizing: border-box; }
  html, body { width: 990px; height: 1200px; overflow: hidden; background: var(--cream); }
  .flyer { position: relative; width: 990px; height: 1200px; overflow: hidden; }
  .backdrop { position: absolute; inset: 0; }

  .badge {
    position: absolute; border-radius: 50%;
    display: flex; flex-direction: column; align-items: center; justify-content: center;
    text-align: center; font-family: "Open Sans", sans-serif; color: var(--white);
  }
  .badge--prizes { left: 428px; top: 128px; width: 140px; height: 140px; background: var(--orange);
    box-shadow: 0 0 0 8px rgba(255,255,255,.85); }
  .badge--prizes .money { font-size: 50px; font-weight: 800; line-height: 1; }
  .badge--prizes .label { font-size: 18px; font-weight: 700; }

  .badge--date { left: 174px; top: 526px; width: 176px; height: 176px; background: var(--orange);
    box-shadow: 0 0 0 8px rgba(255,255,255,.7); }
  .badge--date::before { content: ""; position: absolute; inset: 9px; border: 2px dashed #2d5fae; border-radius: 50%; }
  .badge--date span { font-size: 22px; font-weight: 700; line-height: 1.35; }

  .badge--fee { left: 430px; top: 659px; width: 160px; height: 160px; background: var(--teal);
    box-shadow: 0 0 0 7px var(--white), 0 0 0 11px var(--teal-light); }
  .badge--fee .amount { font-size: 62px; font-weight: 800; line-height: 1; }
  .badge--fee .enter { font-size: 13px; font-weight: 700; margin-top: 2px; }
  .badge--fee .free { font-size: 12px; font-weight: 700; border-top: 2px solid var(--white); margin-top: 6px; padding-top: 4px; line-height: 1.2; }

  .hand { position: absolute; width: 200px; height: 200px; border-radius: 50%;
    box-shadow: 0 0 0 8px var(--white); }
  .hand--left { left: 148px; top: 256px; background: radial-gradient(circle, #fff6e0 0 30%, var(--orange) 32%); }
  .hand--top { left: 658px; top: 151px; background: radial-gradient(circle, #fff6e0 0 30%, var(--teal) 32%);
    box-shadow: 0 0 0 8px var(--white), 0 0 0 16px var(--teal-light); }
  .hand--bottom { left: 665px; top: 441px; background: radial-gradient(circle, #fff6e0 0 30%, var(--teal) 32%);
    box-shadow: 0 0 0 8px var(--white), 0 0 0 16px var(--teal-light); }

  .title { position: absolute; left: 310px; top: 268px; width: 400px; text-align: center;
    font-family: "Oswald", sans-serif; font-weight: 600; line-height: .9; text-transform: uppercase;
    transform: scaleX(.74); transform-origin: 50% 0; }
  .title .rock { display: block; font-size: 130px; color: var(--teal); letter-spacing: -1px; }
  .title .paper { display: block; font-size: 104px; color: var(--orange); }
  .title .scissors { display: block; font-size: 84px; color: var(--teal); }
  .title .event { display: block; font-size: 28px; color: var(--ink); margin-top: 28px; letter-spacing: .5px; }

  .details { position: absolute; left: 0; top: 862px; width: 990px; text-align: center; font-family: "Open Sans", sans-serif; }
  .venue { font-family: "Roboto Condensed", sans-serif; font-weight: 700; font-size: 33px; color: var(--ink); letter-spacing: .5px; }
  .heats { margin-top: 22px; font-size: 19px; font-weight: 700; color: var(--teal); text-transform: uppercase; }
  .extras { margin-top: 6px; font-size: 26px; font-weight: 800; color: var(--orange); text-transform: uppercase; }
  .extras .sep { color: var(--teal); }

  .contact { position: absolute; left: 0; top: 1022px; width: 990px; text-align: center; font-family: "Roboto Condensed", sans-serif; color: var(--ink); }
  .phone { font-size: 58px; font-weight: 400; letter-spacing: 1px; line-height: 1.1; }
  .web { font-size: 28px; }

  .venue-mark { position: absolute; left: 120px; top: 1030px; width: 180px; text-align: center;
    font-family: "Roboto Condensed", sans-serif; font-weight: 700; font-size: 18px; color: #24456b; line-height: 1.2; }
  .venue-mark .dot { display: block; width: 44px; height: 44px; margin: 0 auto 8px; border-radius: 50%; background: #24456b; }
  .county-seal { position: absolute; left: 762px; top: 1006px; width: 140px; height: 140px; border-radius: 50%;
    background: #c9a449; box-shadow: 0 0 0 4px #1f5da4; }
</style>
</head>
<body>
<main class="flyer">
  <svg class="backdrop" width="990" height="1200" viewBox="0 0 990 1200" aria-hidden="true">
    <rect width="990" height="1200" fill="#eef6d6"/>
    <polygon points="0,0 990,0 990,860 0,980" fill="#8fd39a"/>
    <polygon points="0,0 560,0 0,420" fill="#1aa899"/>
    <polygon points="0,0 380,0 0,220" fill="#39bfae"/>
    <polygon points="560,0 990,0 990,520" fill="#9fdc8d"/>
    <polygon points="700,0 990,0 990,260" fill="#cde96a"/>
    <polygon points="0,420 560,0 520,780 0,760" fill="#23b29f" opacity=".75"/>
    <polygon points="300,0 700,0 520,760" fill="#d4e94e"/>
    <polygon points="520,760 990,420 990,860" fill="#b7d83a"/>
    <polygon points="0,640 520,760 0,980" fill="#a9d545"/>
    <polygon points="620,0 990,140 990,420 520,760" fill="#7bcf9f" opacity=".6"/>
    <polygon points="0,1000 990,800 990,1200 0,1200" fill="#f2f8e0"/>
    <polygon points="0,980 990,860 990,900 0,1030" fill="#ffffff" opacity=".5"/>
    <circle cx="510" cy="455" r="290" fill="none" stroke="#ffffff" stroke-width="3" opacity=".5"/>
    <circle cx="510" cy="455" r="250" fill="none" stroke="#d8ec48" stroke-width="10"/>
    <circle cx="510" cy="455" r="236" fill="#ffffff"/>
    <circle cx="250" cy="356" r="118" fill="none" stroke="#f7c94e" stroke-width="4"/>
  </svg>

  <div class="badge badge--prizes"><span class="money">$$$</span><span class="label">PRIZES</span></div>

  <div class="hand hand--left" role="img" aria-label="Illustration: hand showing paper against a fist"></div>
  <div class="hand hand--top" role="img" aria-label="Illustration: fist against a scissors hand"></div>
  <div class="hand hand--bottom" role="img" aria-label="Illustration: scissors hand against an open hand"></div>

  <h1 class="title">
    <span class="rock">Rock</span>
    <span class="paper">Paper</span>
    <span class="scissors">Scissors</span>
    <span class="event">Championship</span>
  </h1>

  <div class="badge badge--date"><span>JUNE 9TH</span><span>2018</span><span>11AM-4PM</span></div>

  <div class="badge badge--fee">
    <span class="amount">$2</span>
    <span class="enter">TO ENTER</span>
    <span class="free">FREE FOR<br>SPECTATORS</span>
  </div>

  <section class="details">
    <p class="venue">BELVORROW SPORTS CENTER, ROSELLE NJ</p>
    <p class="heats">Heats to determine the overall ‘Rock, Paper, Scissors’ champion!</p>
    <p class="extras">Cash prizes <span class="sep">|</span> Live music <span class="sep">|</span> Food and beverage</p>
  </section>

  <div class="venue-mark"><span class="dot"></span>Belvorrow Sports Center</div>

  <section class="contact">
    <p class="phone">908-555-3162</p>
    <p class="web">www.belvorrowgrounds.example</p>
  </section>

  <div class="county-seal" role="img" aria-label="County seal"></div>
</main>
</body>
</html>
```